Company business card

We need a new business card design. We are IT company which is specialized for outsourcing of operations hardware and software (specially Velbrandt, we are a partner), developing custom applications and web applications, BPM solutions, auditing hw and sw. actually design was attached. But we need completely NEW.

Industry/Entity Type

Business

```html
<!DOCTYPE html>
<html lang="en">
<head>
<meta charset="utf-8">
<title>KORVEX business card</title>
<link rel="stylesheet" href="https://fonts.googleapis.com/css2?family=Open+Sans:wght@400;600;700;800&display=swap">
<style>
  :root {
    --backdrop: #2b2b2c;
    --card: #1b1b1d;
    --card-edge: #262628;
    --brand-blue: #1b7fcf;
    --text-light: #e6e6e6;
    --white: #ffffff;
  }
  * { margin: 0; padding: 0; box-sizing: border-box; }
  html, body {
    width: 1200px; height: 900px; overflow: hidden;
    background: var(--backdrop);
    font-family: "Open Sans", Arial, sans-serif;
  }
  .canvas {
    position: relative; width: 1200px; height: 900px;
    display: flex; align-items: center; justify-content: center; gap: 60px;
  }
  .card {
    position: relative; width: 510px; height: 292px;
    background: var(--card);
    border: 1px solid var(--card-edge);
    border-radius: 22px;
    display: flex; align-items: center;
    overflow: hidden;
  }
  .brand-block {
    display: flex; align-items: center; gap: 14px;
    background: var(--brand-blue);
    padding: 20px 24px;
    flex: none;
  }
  .brand-square { width: 62px; height: 62px; background: var(--white); flex: none; }
  .brand-name {
    font-weight: 800; font-size: 40px; line-height: 1;
    color: var(--white); letter-spacing: 1px;
  }
  .card--front { padding: 0 26px 0 24px; gap: 18px; }
  .card--front .brand-block { padding: 16px 18px; gap: 12px; margin-top: 50px; }
  .card--front .brand-square { width: 52px; height: 52px; }
  .card--front .brand-name { font-size: 32px; }
  .divider { width: 1px; height: 160px; background: var(--brand-blue); flex: none; margin-top: -20px; }
  .contact {
    color: var(--text-light); font-size: 12.5px; line-height: 1.45;
    min-width: 0; white-space: nowrap; margin-top: -20px;
  }
  .contact .person { color: var(--brand-blue); font-weight: 600; font-size: 15px; }
  .contact .role { margin-bottom: 8px; }
  .contact .company { color: var(--brand-blue); font-weight: 600; font-size: 14px; }
  .contact .address { margin-bottom: 8px; }
  .contact-line { display: flex; align-items: center; gap: 7px; }
  .contact-line svg { width: 10px; height: 10px; flex: none; }
  .icon-fill { fill: var(--brand-blue); }
  .icon-stroke { fill: none; stroke: var(--brand-blue); stroke-width: 2.5; }
  .card--back { justify-content: center; }
</style>
</head>
<body>
<main class="canvas">
  <section class="card card--front">
    <div class="brand-block">
      <div class="brand-square"></div>
      <span class="brand-name">KORVEX</span>
    </div>
    <div class="divider"></div>
    <div class="contact">
      <div class="person">Marek Halvan</div>
      <div class="role">CEO</div>
      <div class="company">KORVEX s.r.o</div>
      <div class="address">Lipova 17<br>811 02 Bratislava</div>
      <div class="contact-line">
        <svg viewBox="0 0 24 24"><path class="icon-fill" d="M6.6 10.8a15 15 0 0 0 6.6 6.6l2.2-2.2c.3-.3.7-.4 1-.2 1.1.4 2.3.6 3.6.6.6 0 1 .4 1 1V20c0 .6-.4 1-1 1C10.6 21 3 13.4 3 4c0-.6.4-1 1-1h3.5c.6 0 1 .4 1 1 0 1.3.2 2.5.6 3.6.1.3 0 .7-.2 1z"/></svg>
        <span>+421 (0) 900 555 012</span>
      </div>
      <div class="contact-line">
        <svg viewBox="0 0 24 24"><path class="icon-stroke" d="M3 6h18v12H3z M3 6l9 7 9-7"/></svg>
        <span>marek.halvan@korvex.sk</span>
      </div>
      <div class="contact-line">
        <svg viewBox="0 0 24 24"><circle class="icon-stroke" cx="12" cy="12" r="9"/><path class="icon-stroke" d="M3 12h18 M12 3c3 3 3 15 0 18 M12 3c-3 3-3 15 0 18"/></svg>
        <span>www.korvex.sk</span>
      </div>
    </div>
  </section>
  <section class="card card--back">
    <div class="brand-block">
      <div class="brand-square"></div>
      <span class="brand-name">KORVEX</span>
    </div>
  </section>
</main>
</body>
</html>
```